Re-style home page - eye-catching and unique design for social commerce website

We need a new concept design for TrindaMo's home page.
We don't want to make huge changes but creating a more professional and eye-catching style.

We need to look very serious like a professional services company and in the same time to look like a social network for e-commerce.

Our logo is very captive and you can use to creating something of harmonious.

This is a re-style and I'm excepted to see unique and fresh design like Clovaret.

Target Market(s)

e-commerce and social

Industry/Entity Type

Social

Number of Pages Required

1 page

Font styles to use
Serif
Sans Serif

Requirements
Must have
• An eye-catching result.
• Search bar with logo and Login How it works and business
• The slogan with login and signup.
• Footer links.
Nice to have
• I would like to open the home page and see only two clear ways:
• -Consumer
• --Search
• --The slogan
• --Login and Signup
• --How it works
• -Business
• --Go to Business area
• Background: City, Shopping.
Should not have
• Scrollbar style!

```html
<!DOCTYPE html>
<html lang="en">
<head>
<meta charset="utf-8">
<title>TrindaMo – Home</title>
<link rel="stylesheet" href="https://fonts.googleapis.com/css2?family=Raleway:wght@400;500;600&family=Open+Sans:wght@400;600&display=swap">
<style>
  :root {
    --white: #ffffff;
    --nav-text: #f4f4f4;
    --field-text: #8a8a8a;
    --field-bg: #ffffff;
    --social-blue: #2a4fa8;
    --login-red: #e0342c;
    --signup-blue: #1f3a93;
    --footer-bg: rgba(48, 48, 50, 0.92);
    --footer-text: #e2e2e2;
    --footer-muted: #bdbdbd;
  }
  * { box-sizing: border-box; margin: 0; padding: 0; }
  html, body { width: 1200px; height: 692px; overflow: hidden; }
  body { font-family: "Open Sans", Arial, sans-serif; position: relative; background: #cfc9c4; }

  .hero-photo {
    position: absolute; inset: 0 0 79px 0;
    background:
      radial-gradient(ellipse at 18% 40%, #b98f72 0%, transparent 45%),
      radial-gradient(ellipse at 85% 45%, #8aa2bd 0%, transparent 45%),
      radial-gradient(ellipse at 55% 85%, #8d7a86 0%, transparent 50%),
      linear-gradient(180deg, #d9d6d2 0%, #b9aba3 60%, #8b7e80 100%);
  }

  .site-header { position: absolute; top: 0; left: 0; width: 1200px; height: 100px; }
  .brand {
    position: absolute; left: 230px; top: 30px; display: flex; align-items: center; gap: 8px;
    font-family: "Raleway", sans-serif; font-weight: 600; font-size: 36px; color: var(--white);
  }
  .brand-dot { width: 14px; height: 14px; border-radius: 50%; background: var(--login-red); }
  .search {
    position: absolute; left: 487px; top: 40px; width: 214px; height: 26px;
    background: var(--field-bg); display: flex; align-items: center; padding: 0 8px 0 11px;
  }
  .search span { flex: 1; font-size: 9px; color: var(--field-text); }
  .main-nav { position: absolute; top: 41px; left: 733px; display: flex; gap: 28px; }
  .main-nav a { font-family: "Raleway", sans-serif; font-size: 14.5px; color: var(--nav-text); text-decoration: none; }

  .signup-panel {
    position: absolute; left: 343px; top: 173px; width: 514px; height: 299px;
    box-shadow: 0 2px 10px rgba(0,0,0,.35); overflow: hidden;
  }
  .panel-photo {
    position: absolute; inset: 0;
    background:
      radial-gradient(ellipse at 30% 60%, #c9a687 0%, transparent 50%),
      radial-gradient(ellipse at 80% 70%, #6f7fa6 0%, transparent 45%),
      linear-gradient(180deg, #d8c6ae 0%, #a49487 55%, #5e5872 100%);
  }
  .panel-content { position: relative; text-align: center; color: var(--white); }
  .panel-title { font-family: "Raleway", sans-serif; font-weight: 500; font-size: 30px; margin-top: 31px; line-height: 34px; }
  .panel-sub { font-family: "Raleway", sans-serif; font-size: 17px; line-height: 20px; }
  .btn-social {
    display: flex; align-items: center; justify-content: center;
    width: 211px; height: 32px; margin: 12px auto 0; background: var(--social-blue);
    color: var(--white); font-weight: 600; font-size: 12px;
  }
  .divider { font-family: "Raleway", sans-serif; font-size: 14px; line-height: 20px; margin: 2px 0 4px; }
  .field {
    width: 211px; height: 33px; margin: 0 auto 8px; background: var(--field-bg);
    text-align: left; padding-left: 10px; line-height: 33px; font-size: 10px; color: var(--field-text);
  }
  .actions { display: flex; justify-content: center; align-items: center; gap: 8px; }
  .btn { width: 89px; height: 31px; line-height: 31px; color: var(--white); font-family: "Raleway", sans-serif; font-size: 15px; }
  .btn-login { background: var(--login-red); margin-left: 2px; }
  .btn-signup { background: var(--signup-blue); margin-left: 6px; }
  .actions .divider { margin: 0 6px 0 0; }

  .slider-dots { position: absolute; top: 574px; left: 569px; display: flex; gap: 7px; }
  .slider-dots i { width: 14px; height: 14px; border-radius: 50%; background: rgba(255,255,255,.45); }
  .slider-dots i.active { background: var(--white); }

  .site-footer { position: absolute; left: 0; bottom: 0; width: 1200px; height: 79px; background: var(--footer-bg); }
  .footer-links { position: absolute; left: 223px; top: 28px; font-size: 11.5px; color: var(--footer-text); }
  .footer-links a { color: var(--footer-text); text-decoration: none; }
  .footer-links .sep { margin: 0 7px; color: var(--footer-muted); }
  .copyright { position: absolute; left: 223px; top: 52px; font-size: 9.5px; color: var(--footer-muted); }
  .social-links { position: absolute; right: 250px; top: 30px; display: flex; gap: 10px; font-size: 10px; font-weight: 600; color: var(--footer-text); }
</style>
</head>
<body>
  <div class="hero-photo" role="img" aria-label="Photo of a group of young friends sharing a tablet outdoors, city shopping mood"></div>

  <header class="site-header">
    <div class="brand"><span>TrindaMo</span><span class="brand-dot"></span></div>
    <div class="search">
      <span>Search here</span>
      <svg width="14" height="14" viewBox="0 0 14 14"><circle cx="5.8" cy="5.8" r="4.3" fill="none" stroke="#666" stroke-width="1.8"/><line x1="9" y1="9" x2="13" y2="13" stroke="#666" stroke-width="2" stroke-linecap="round"/></svg>
    </div>
    <nav class="main-nav">
      <a href="#">Login</a>
      <a href="#">How it Works</a>
      <a href="#">Business</a>
    </nav>
  </header>

  <section class="signup-panel">
    <div class="panel-photo" role="img" aria-label="Photo of friends with shopping bags looking at a phone"></div>
    <div class="panel-content">
      <h1 class="panel-title">Mauris lacus felis vestibulum</h1>
      <p class="panel-sub">Cum sociis natoque penatibus et magnis dis parturient</p>
      <div class="btn-social">Continue with Konnekta</div>
      <p class="divider">or</p>
      <div class="field">Email</div>
      <div class="field">Create Password</div>
      <div class="actions">
        <div class="btn btn-login">Login</div>
        <span class="divider">or</span>
        <div class="btn btn-signup">Sign up</div>
      </div>
    </div>
  </section>

  <div class="slider-dots"><i class="active"></i><i></i><i></i><i></i></div>

  <footer class="site-footer">
    <nav class="footer-links">
      <a href="#">About us</a><span class="sep">|</span><a href="#">Blog</a><span class="sep">|</span><a href="#">Business</a><span class="sep">|</span><a href="#">Jobs</a><span class="sep">|</span><a href="#">Privacy</a><span class="sep">|</span><a href="#">FAQ</a><span class="sep">|</span><a href="#">Contacts</a>
    </nav>
    <p class="copyright">© 2015 Company Name &nbsp;All right reserved &nbsp;Term of Use</p>
    <div class="social-links"><span>Chirpa</span><span>Konnekta</span><span>Worknet</span></div>
  </footer>
</body>
</html>
```